IT Company based on Biology Business Needs a Business Card Design

We need a business card design for a new company called 'Lumen CELL'. We develop the machine learning solutions especially focused on deep learning algorithms for biology industry. Our initial product is a vision detection on biological images to help doctors diagnose the symptoms. We would like to see designs that use the color green.

Industry/Entity Type

Business

```html
<!DOCTYPE html>
<html lang="en">
<head>
<meta charset="utf-8">
<title>Lumen CELL — Business Card</title>
<link rel="stylesheet" href="https://fonts.googleapis.com/css2?family=Open+Sans:wght@400;600;700&display=swap">
<style>
  :root {
    --backdrop: #151515;
    --paper: #f2f2f2;
    --leaf: #7cc242;
    --leaf-deep: #6ab533;
    --emerald: #12a24f;
    --emerald-light: #1db862;
    --brand-green: #3fae3c;
    --ink-light: #ffffff;
  }
  * { margin: 0; padding: 0; box-sizing: border-box; }
  html, body {
    width: 1200px; height: 840px; overflow: hidden;
    background: var(--backdrop);
    font-family: "Open Sans", Arial, sans-serif;
  }
  .canvas { position: relative; width: 1200px; height: 840px; }

  .card {
    position: absolute;
    width: 540px; height: 309px;
    border-radius: 3px;
    overflow: hidden;
    box-shadow: 0 18px 40px rgba(0,0,0,0.6);
  }

  /* Back of card: contact side */
  .card-contact {
    left: 600px; top: 90px;
    display: flex;
    background: var(--paper);
  }
  .contact-brand {
    width: 52%;
    display: flex; align-items: center; justify-content: center;
    gap: 10px;
  }
  .brand-dot {
    width: 16px; height: 16px; border-radius: 50%;
    background: var(--brand-green);
  }
  .brand-name {
    font-weight: 600; font-size: 34px; letter-spacing: -1px;
    color: var(--brand-green);
  }
  .contact-panel {
    width: 48%;
    background: linear-gradient(160deg, var(--leaf), var(--leaf-deep));
    color: var(--ink-light);
    padding: 40px 24px 0 26px;
  }
  .person-name { font-weight: 700; font-size: 14px; letter-spacing: 0.2px; }
  .person-role { font-size: 12px; margin-top: 2px; }
  .address { font-size: 12px; margin-top: 22px; }
  .contact-list { list-style: none; margin-top: 48px; }
  .contact-list li {
    display: flex; align-items: center; gap: 8px;
    font-size: 12.5px; margin-bottom: 6px;
  }
  .contact-icon {
    width: 15px; height: 15px; border-radius: 50%;
    background: rgba(255,255,255,0.85);
    color: var(--leaf-deep);
    font-size: 9px; font-weight: 700;
    display: flex; align-items: center; justify-content: center;
  }

  /* Front of card: brand side */
  .card-brand {
    left: 90px; top: 440px;
    background: linear-gradient(135deg, var(--emerald), var(--emerald-light) 55%, var(--emerald));
    display: flex; align-items: center; justify-content: center;
    gap: 14px;
  }
  .card-brand .brand-dot { width: 22px; height: 22px; background: var(--ink-light); }
  .card-brand .brand-name { font-size: 48px; color: var(--ink-light); }
</style>
</head>
<body>
<main class="canvas">
  <section class="card card-contact">
    <div class="contact-brand">
      <span class="brand-dot"></span>
      <span class="brand-name">LUMEN CELL</span>
    </div>
    <div class="contact-panel">
      <p class="person-name">YOUR NAME GOES HERE</p>
      <p class="person-role">Designation</p>
      <p class="address">Your address goes here</p>
      <ul class="contact-list">
        <li><span class="contact-icon">p</span>012345678</li>
        <li><span class="contact-icon">e</span>aaabbb@lumencell.com</li>
        <li><span class="contact-icon">w</span>www.lumencell.com</li>
      </ul>
    </div>
  </section>

  <section class="card card-brand">
    <span class="brand-dot"></span>
    <span class="brand-name">LUMEN CELL</span>
  </section>
</main>
</body>
</html>
```